WTF!!! We need a modern professional website for a business litigation law firm.

We need a modern, clean, professional and uncomplicated website for a new business trial and litigation law firm called "Hallorand Trial Firm PLLC". Website must be mobile optimized for iPad and smartphone. The law firm specializes in counseling and representing large corporations, small businesses and entrepreneurs in and out of the courtroom. Lawyers in the firm serve as Florida counsel and trial counsel to organizations facing claims involving product liability, premises liability, professional liability, vehicle and transportation liability, warranty claims, construction defects and delay claims, complex business disputes, commercial litigation and bid disputes in State and Federal Courts. The website is mainly to provide information about the firm, and should include sections describing the firm, identifying the Industries Served and Areas of Practice ," a separate page identifying the "Professionals", a separate page for "Resources & Advisories," and a traveling "Connect With Us" button a site visitor can click on that will launch an email to the Firm's general email account. The website should allow us to easily modify the content on these pages, and let us add/modify links to external information sources. We will not sell anything or take payments through the website. We do need to be able to easily upload and update photographs of attorneys and add new attorneys names/email hyperlinks as the firm grows. We would like to add developments in the law or success stories easily and quickly, such as through a blog page. On the "Connect With Us" page the website should have hyperlinks to email the Firm, and there should be hyperlinks to email each professional on the "Professionals" page. The website should be viewable on mobile devices without distortion. The law firm focuses on trial work and should have some imagery associated with courtrooms, but the overall theme of the site should be modern, clean, and communicate sophistication and strength. The website should be made in Wordpress. We have uploaded logo files for Hallorand Trial Firm.

Target Market(s)

Corporations and companies that are looking for legal representation. Other attorneys/legal industry.

Industry/Entity Type

Legal Industry

Coding

Coded - Design and coding required

Number of Pages Required

1 page

Font styles to use
Sans Serif

Requirements
Must have
• Simple, clean, sophisticated, modern website that includes the logo, watermark of logo, and the elements described above.
Nice to have
• Pictures of city scape, buildings, courtroom, team members.

```html
<!DOCTYPE html>
<html lang="en">
<head>
<meta charset="utf-8">
<title>Hallorand Trial Firm PLLC</title>
<link rel="stylesheet" href="https://fonts.googleapis.com/css2?family=DM+Serif+Display&family=Montserrat:wght@400;500;600;700&display=swap">
<style>
:root{
  --gold:#c49a6c;
  --gold-soft:#e8d6c2;
  --ink:#222222;
  --text:#444444;
  --navy:#0f1a33;
  --line:#e3e3e3;
  --white:#ffffff;
}
*{margin:0;padding:0;box-sizing:border-box}
html,body{width:1200px;height:3209px;overflow:hidden}
body{position:relative;background:var(--white);font-family:'Montserrat',sans-serif;color:var(--text)}
.abs{position:absolute}
.serif{font-family:'DM Serif Display',serif;font-weight:400}
.btn{position:absolute;background:var(--gold);color:var(--white);font-weight:700;font-size:12px;border-radius:4px;display:flex;align-items:center;justify-content:center}
.eyebrow{position:absolute;color:var(--gold);font-size:14px;font-weight:500;display:flex;align-items:center;gap:8px}
.eyebrow::before,.eyebrow.both::after{content:"";width:22px;height:1px;background:var(--gold)}
.eyebrow.both::after{width:50px}
.section-title{position:absolute;font-family:'DM Serif Display',serif;color:var(--ink);font-size:31px;line-height:1}

/* hero */
.hero{position:absolute;left:0;top:0;width:1200px;height:632px;background:linear-gradient(100deg,#2b2824 0%,#4a4239 45%,#6f6a63 75%,#3c3935 100%)}
.hero-shade{position:absolute;inset:0;background:linear-gradient(90deg,rgba(20,18,15,.55),rgba(20,18,15,.1))}
.topbar{position:absolute;left:0;top:0;width:1200px;height:25px;background:rgba(20,18,15,.55);color:var(--white);font-size:12px}
.topbar span{position:absolute;top:6px}
.brand{position:absolute;left:100px;top:34px;color:var(--white);font-weight:700;font-size:15px;line-height:17px;letter-spacing:1px;display:flex;align-items:center;gap:8px}
.brand i{width:12px;height:12px;background:var(--gold);display:block}
.nav{position:absolute;top:56px;left:578px;display:flex;gap:24px;color:#e5e5e5;font-size:11px;font-weight:500}
.nav .on{color:var(--white);font-weight:700}
.hero-tag{position:absolute;left:97px;top:233px;color:#e8e8e8;font-size:12px;display:flex;align-items:center;gap:8px}
.hero-tag::before{content:"";width:22px;height:1px;background:#e8e8e8}
.hero h1{position:absolute;left:100px;top:252px;color:var(--white);font-size:41px;line-height:48px;font-family:'DM Serif Display',serif;font-weight:400}

/* about */
.about-text{position:absolute;left:100px;width:440px;font-size:12px;line-height:15px;color:var(--text)}
.photo{position:absolute}

/* practice */
.frame-line{position:absolute;background:var(--gold-soft)}
.card{position:absolute;width:281px;height:172px;border:1px solid var(--line);padding:12px}
.card svg{display:block}
.card h3{color:var(--gold);font-size:14px;font-weight:600;margin:12px 0 8px}
.card p{font-size:10.5px;line-height:13px;color:var(--text);height:40px}
.card .btn{position:static;width:84px;height:24px;font-size:11px;margin-top:14px}

/* blog */
.post{position:absolute;top:2259px;width:232px;height:231px;border:1px solid var(--gold-soft);border-radius:10px;padding:12px}
.post .img{height:123px;border-radius:8px}
.post .date{color:var(--gold);font-size:10px;margin-top:11px}
.post h4{color:var(--ink);font-size:12px;font-weight:700;line-height:15px;margin-top:10px}
.post .more{color:var(--gold);font-size:10.5px;font-weight:600;margin-top:8px}

/* contact */
.field{position:absolute;border:1px solid var(--line);font-size:11px;color:#555;padding:7px 12px}
.info{position:absolute;left:639px;width:446px;height:58px;border:1px solid var(--line)}
.info svg{position:absolute;left:15px;top:17px}
.info .t{position:absolute;left:60px;top:7px;font-family:'DM Serif Display',serif;color:var(--gold);font-size:19px}
.info .d{position:absolute;left:60px;top:33px;font-size:14px;color:var(--ink)}

/* footer */
.footer{position:absolute;left:0;top:2934px;width:1200px;height:275px;background:var(--navy);color:var(--white)}
.footer .brand{left:100px;top:76px;font-size:24px;line-height:28px}
.fcol{position:absolute;top:66px;font-size:13px;line-height:27px}
.fcol h5{font-size:14px;font-weight:700;margin-bottom:2px}
</style>
</head>
<body>

<!-- Hero -->
<header class="hero">
  <div class="abs" role="img" aria-label="Photo of two attorneys in suits talking in a bright office" style="inset:0"></div>
  <div class="hero-shade"></div>
  <div class="topbar">
    <span style="left:100px">Mon-Sat 9am-8pm</span>
    <span style="left:798px">info@hallorandtrialfirm.com</span>
    <span style="left:1001px">214 Corbel Lane</span>
  </div>
  <div class="brand"><i></i><span>HALLORAND<br>TRIAL FIRM</span></div>
  <nav class="nav">
    <span class="on">Home</span><span>About Us</span><span>Industry Served</span><span>Practice Area</span><span>Blog</span><span>Faqs</span>
  </nav>
  <div class="btn" style="left:1014px;top:51px;width:86px;height:25px;font-size:11px">Contact Us</div>
  <div class="hero-tag">The law firm specializes in counseling and representing large corporations,</div>
  <h1>Experienced Trial Attorneys<br>Fighting For Your Success</h1>
  <div class="btn" style="left:100px;top:364px;width:172px;height:29px">Book free Consultation</div>
</header>

<!-- About -->
<section>
  <div class="eyebrow" style="left:100px;top:703px">About Us<span style="width:100px;height:1px;background:var(--gold-soft);display:block"></span></div>
  <h2 class="section-title" style="left:100px;top:727px">Hallorand Trial Firm PLL</h2>
  <p class="about-text" style="top:774px">At Hallorand Trial Firm PLLC, we are dedicated to providing exceptional legal counsel to businesses and organizations across a wide range of industries. Our core values of integrity, dedication, and strategic thinking shape everything we do, from advising clients to representing them in the courtroom. We approach each case with a commitment to achieving the best possible outcome, always focused on delivering results with the utmost professionalism.</p>
  <p class="about-text" style="top:894px">Our vision is to be the trusted partner for businesses navigating complex legal challenges, combining deep legal expertise with a client-centered approach. Whether in or out of the courtroom, we pride ourselves on delivering effective and timely solutions that safeguard our clients' interests and protect their reputations.</p>
  <div class="btn" style="left:100px;top:990px;width:100px;height:29px">Learn More</div>
  <div class="photo" role="img" aria-label="Photo of two colleagues reviewing documents on a tablet at a desk" style="left:791px;top:706px;width:309px;height:298px;background:linear-gradient(135deg,#4f8a8c,#9cb3b0 45%,#7a5a3c)"></div>
  <div class="photo" role="img" aria-label="Photo of an older attorney and a client signing papers at a table" style="left:584px;top:847px;width:255px;height:177px;background:linear-gradient(120deg,#3a2c22,#cfc7bd 45%,#efeae4);border:6px solid #fff;border-left:0;border-bottom:0"></div>
</section>

<!-- Practice -->
<section>
  <div class="frame-line" style="left:100px;top:1108px;width:481px;height:1px"></div>
  <div class="frame-line" style="left:100px;top:1108px;width:1px;height:103px"></div>
  <div class="frame-line" style="left:1100px;top:1582px;width:1px;height:104px"></div>
  <div class="frame-line" style="left:619px;top:1686px;width:482px;height:1px"></div>
  <div class="eyebrow both" style="left:135px;top:1153px">Our Practice Area</div>
  <h2 class="section-title" style="left:135px;top:1178px;font-size:29px">We Specialized In</h2>
  <p class="abs" style="left:592px;top:1147px;width:460px;font-size:12px;line-height:15px">We assist manufacturers, suppliers, and distributors in defending against claims related to defective products. Our attorneys have a proven track record in handling high-stakes product liability cases, ensuring that our clients are protected from unwarranted claims and reputational damage.</p>

  <div class="card" style="left:135px;top:1246px">
    <svg width="32" height="32" viewBox="0 0 32 32"><rect x="3" y="8" width="18" height="18" fill="none" stroke="#c49a6c" stroke-width="2"/><circle cx="23" cy="22" r="6" fill="none" stroke="#c49a6c" stroke-width="2"/></svg>
    <h3>Product Liability</h3>
    <p>We assist manufacturers, suppliers, and distributors in defending against claims related to defective products.</p>
    <div class="btn">View More</div>
  </div>
  <div class="card" style="left:450px;top:1246px">
    <svg width="32" height="32" viewBox="0 0 32 32"><path d="M12 4a6 6 0 0 1 6 6c0 5-6 11-6 11s-6-6-6-11a6 6 0 0 1 6-6z" fill="none" stroke="#c49a6c" stroke-width="2"/><rect x="4" y="24" width="24" height="5" fill="none" stroke="#c49a6c" stroke-width="2"/></svg>
    <h3>Premises Liability</h3>
    <p>We represent property owners and businesses in cases involving injuries sustained on their premises.</p>
    <div class="btn">View More</div>
  </div>
  <div class="card" style="left:766px;top:1246px">
    <svg width="32" height="32" viewBox="0 0 32 32"><path d="M5 29V4h4v25M5 6h22M23 6v8M15 29V18h12v11" fill="none" stroke="#c49a6c" stroke-width="2"/></svg>
    <h3>Construction &amp; Development</h3>
    <p>Our firm is well-versed in handling construction defect claims, delays, and disputes.</p>
    <div class="btn">View More</div>
  </div>
  <div class="card" style="left:135px;top:1449px">
    <svg width="32" height="32" viewBox="0 0 32 32"><circle cx="16" cy="16" r="9" fill="none" stroke="#c49a6c" stroke-width="2"/><circle cx="16" cy="16" r="3" fill="#c49a6c"/><path d="M16 3v4M16 25v4M3 16h4M25 16h4" stroke="#c49a6c" stroke-width="2"/></svg>
    <h3>Commercial Litigation</h3>
    <p>We help businesses resolve a wide range of commercial disputes, from breach of contract to shareholder disputes.</p>
    <div class="btn">View More</div>
  </div>
  <div class="card" style="left:450px;top:1449px">
    <svg width="32" height="32" viewBox="0 0 32 32"><rect x="3" y="10" width="15" height="13" fill="none" stroke="#c49a6c" stroke-width="2"/><path d="M18 14h6l4 5v4H18z" fill="none" stroke="#c49a6c" stroke-width="2"/><circle cx="9" cy="25" r="2.5" fill="#c49a6c"/><circle cx="23" cy="25" r="2.5" fill="#c49a6c"/></svg>
    <h3>Transportation &amp; Vehicle Liability</h3>
    <p>We defend transportation and logistics companies in cases involving accidents, vehicle liability, and regulatory compliance.</p>
    <div class="btn">View More</div>
  </div>
  <div class="card" style="left:766px;top:1449px">
    <svg width="32" height="32" viewBox="0 0 32 32"><rect x="7" y="3" width="18" height="26" rx="2" fill="none" stroke="#c49a6c" stroke-width="2"/><path d="M11 11h10M11 16h10M11 21h6" stroke="#c49a6c" stroke-width="2"/></svg>
    <h3>Warranty Claims</h3>
    <p>We assist manufacturers, suppliers, and distributors in defending against claims.</p>
    <div class="btn">View More</div>
  </div>
</section>

<!-- Team -->
<section>
  <div class="eyebrow both" style="left:503px;top:1759px">Our Team</div>
  <h2 class="section-title" style="left:0;width:1196px;text-align:center;top:1782px">Our Professional Team</h2>
  <div class="photo" role="img" aria-label="Portrait of a senior attorney in a dark suit" style="left:99px;top:1856px;width:188px;height:204px;background:linear-gradient(160deg,#5a3a26,#2a221d)"></div>
  <div class="photo" role="img" aria-label="Portrait of an attorney signing papers at a desk" style="left:303px;top:1856px;width:187px;height:204px;background:linear-gradient(160deg,#eef0f1,#c8ccd0 60%,#3a3d44)"></div>
  <div class="photo" role="img" aria-label="Portrait of an associate holding a tablet" style="left:506px;top:1856px;width:188px;height:204px;background:linear-gradient(160deg,#b07b4c,#e7e1d8 55%,#2c2a2a)"></div>
  <div class="photo" role="img" aria-label="Portrait of an attorney in an office" style="left:710px;top:1856px;width:187px;height:204px;background:linear-gradient(160deg,#cfcbc6,#8e8a86 55%,#262626)"></div>
  <div class="photo" role="img" aria-label="Portrait of a young attorney in a suit and tie" style="left:913px;top:1856px;width:188px;height:204px;background:linear-gradient(160deg,#2f5d93,#8aa6c2 50%,#1d2330)"></div>
  <div class="abs serif" style="left:111px;top:2072px;color:var(--gold);font-size:14px">Renata Ostrow</div>
  <div class="abs" style="left:111px;top:2091px;color:var(--ink);font-size:12px;font-weight:500">Associate</div>
</section>

<!-- Blog -->
<section>
  <div class="eyebrow" style="left:100px;top:2173px">Articles &amp; Blog<span style="width:44px;height:1px;background:var(--gold);display:block"></span></div>
  <h2 class="section-title" style="left:100px;top:2197px">Our Blogs &amp; Articles</h2>
  <div class="btn" style="left:1027px;top:2197px;width:73px;height:28px">See All</div>
  <article class="post" style="left:100px">
    <div class="img" role="img" aria-label="Photo of a wooden gavel on contract papers" style="background:linear-gradient(135deg,#8a4a28,#c9a58a 45%,#e9e2d8)"></div>
    <div class="date">24 January 2025</div>
    <h4>Recent Changes in Florida's Product Liability Laws</h4>
    <div class="more">Read More</div>
  </article>
  <article class="post" style="left:356px">
    <div class="img" role="img" aria-label="Photo of a judge's gavel on a desk" style="background:linear-gradient(135deg,#e8b86a,#7a6244 50%,#2a2520)"></div>
    <div class="date">24 January 2025</div>
    <h4>Recent Changes in Florida's Product Liability Laws</h4>
    <div class="more">Read More</div>
  </article>
  <article class="post" style="left:612px">
    <div class="img" role="img" aria-label="Photo of a person signing a document" style="background:linear-gradient(160deg,#2c3e63,#6b7da0 45%,#e9ebef)"></div>
    <div class="date">24 January 2025</div>
    <h4>Recent Changes in Florida's Product Liability Laws</h4>
    <div class="more">Read More</div>
  </article>
  <article class="post" style="left:868px">
    <div class="img" role="img" aria-label="Photo of an attorney standing in a law library" style="background:linear-gradient(135deg,#6d6a62,#3d3a35 50%,#1f1d1b)"></div>
    <div class="date">24 January 2025</div>
    <h4>Recent Changes in Florida's Product Liability Laws</h4>
    <div class="more">Read More</div>
  </article>
</section>

<!-- Contact -->
<section>
  <div class="eyebrow both" style="left:115px;top:2561px">Connect With Us</div>
  <h2 class="section-title" style="left:115px;top:2585px;font-size:30px">Send Us Message</h2>
  <div class="field" style="left:115px;top:2647px;width:226px;height:27px">Name</div>
  <div class="field" style="left:364px;top:2647px;width:227px;height:27px">Phone</div>
  <div class="field" style="left:115px;top:2689px;width:476px;height:27px">Email</div>
  <div class="field" style="left:115px;top:2732px;width:476px;height:74px">Write A Message</div>
  <div class="btn" style="left:115px;top:2821px;width:118px;height:29px">Send Message</div>

  <div class="eyebrow both" style="left:639px;top:2561px">Get In Touch</div>
  <h2 class="section-title" style="left:639px;top:2585px;font-size:30px">Free Consultation</h2>
  <div class="info" style="top:2643px">
    <svg width="26" height="26" viewBox="0 0 24 24"><path d="M6.6 10.8a15 15 0 0 0 6.6 6.6l2.2-2.2a1 1 0 0 1 1-.25 11.4 11.4 0 0 0 3.6.57 1 1 0 0 1 1 1V20a1 1 0 0 1-1 1A17 17 0 0 1 3 4a1 1 0 0 1 1-1h3.5a1 1 0 0 1 1 1c0 1.25.2 2.45.57 3.57a1 1 0 0 1-.25 1z" fill="#c49a6c"/></svg>
    <div class="t">Call Us Today</div><div class="d">(406) 555-0187</div>
  </div>
  <div class="info" style="top:2721px">
    <svg width="26" height="26" viewBox="0 0 24 24"><rect x="2" y="5" width="20" height="14" rx="2" fill="#c49a6c"/><path d="M3 6l9 7 9-7" fill="none" stroke="#fff" stroke-width="1.6"/></svg>
    <div class="t">Call Us Today</div><div class="d">Mara.Lenz@Example.Com</div>
  </div>
  <div class="info" style="top:2799px">
    <svg width="26" height="26" viewBox="0 0 24 24"><path d="M12 2a7 7 0 0 1 7 7c0 5.2-7 13-7 13S5 14.2 5 9a7 7 0 0 1 7-7z" fill="#c49a6c"/><circle cx="12" cy="9" r="2.6" fill="#fff"/></svg>
    <div class="t">Call Us Today</div><div class="d">1186 Larkspur Ave. Dayton, Ohio 45402</div>
  </div>
</section>

<!-- Footer -->
<footer class="footer">
  <div class="brand"><i style="width:16px;height:16px"></i><span>HALLORAND<br>TRIAL FIRM</span></div>
  <div class="fcol" style="left:376px"><h5>Links</h5>Our Team<br>Team Member<br>Get In Touch<br>Contact Us<br>About Us</div>
  <div class="fcol" style="left:581px"><h5>Contact</h5>(406) 555-0187<br>Mara.Lenz@Example.Com<br><span style="display:block;line-height:16px;margin-top:5px">1186 Larkspur Ave.<br>Dayton, Ohio 45402</span></div>
  <div class="fcol" style="left:856px"><h5>Prectice Area</h5>Product Liability<br>Premises Liability<br>Construction &amp; Development<br>Commercial Litigation<br>Transportation &amp; Vehicle Liability</div>
</footer>

</body>
</html>
```